Ripple (nightclub flyer)

Nightclub flyer, guaranteed project. Text below (and please use logos, large):

RIPPLE PRESENTS:

KORVEN (LOGO) B2B MARTIN VOLKE (LOGO)

+TREVV LANE (smaller text)

10/26/17

2284 HARLOW AVENUE SACRAMENTO CA
21+ 10PM-2AM

HOUSE/TECHNO

A BLUE CASCADE ENTERTAINMENT (LOGO) PRODUCTION

Target Market(s)

House/Electronic Music Lovers

Industry/Entity Type

Night Club

Font styles to use
Sans Serif

Colors

Designer to choose colors to be used in the design.

Requirements
Must have
• Large logos for the dj names, or large block letter dj names (logos not necessary if it looks better without. But KORVEN b2b MARTIN VOLKE large and TREVV LANE smaller on separate line
Nice to have
• Can include a classy female model but nothing cheesy or too sexy

```html
<!DOCTYPE html>
<html lang="en">
<head>
<meta charset="utf-8">
<title>Ripple – Nightclub Flyer</title>
<link rel="stylesheet" href="https://fonts.googleapis.com/css2?family=Audiowide&family=Exo+2:wght@700;800&family=Saira+Semi+Condensed:wght@600;700&family=Black+Ops+One&display=swap">
<style>
  :root {
    --backdrop: #dcdcd9;
    --ink-black: #020607;
    --teal-deep: #062326;
    --teal-mid: #0d4a4d;
    --teal-glow: #1f8a8c;
    --cyan: #5fd6ec;
    --sky: #3aa8e6;
    --white: #f4fbfc;
    --muted: #9fc4c8;
  }
  * { box-sizing: border-box; margin: 0; padding: 0; }
  html, body {
    width: 1200px; height: 900px; overflow: hidden;
    background: var(--backdrop);
  }
  .flyer {
    position: absolute; left: 303px; top: 30px;
    width: 594px; height: 840px; overflow: hidden;
    background: linear-gradient(180deg, var(--ink-black) 0%, var(--teal-deep) 30%, var(--teal-mid) 58%, #0a3b3c 74%, var(--ink-black) 80%);
    box-shadow: 0 18px 40px rgba(0,0,0,.25);
  }
  .flyer__shapes { position: absolute; inset: 0; }
  .flyer__photo {
    position: absolute; left: 112px; top: 40px; width: 370px; height: 390px;
    background: radial-gradient(ellipse at 50% 40%, #3f8e93 0%, #1b5357 45%, rgba(8,40,43,0) 75%);
  }
  .genre {
    position: absolute; left: 0; right: 0; top: 56px; text-align: center;
    font: 400 20px/1 "Audiowide", sans-serif; letter-spacing: 1px;
    color: var(--cyan);
  }
  .host {
    position: absolute; left: 0; right: 0; top: 386px; text-align: center;
    font: 800 64px/1 "Exo 2", sans-serif; color: var(--white);
    text-shadow: 0 0 18px rgba(95,214,236,.7);
  }
  .presents {
    position: absolute; left: 0; right: 0; top: 458px; text-align: center;
    font: 700 16px/1 "Saira Semi Condensed", sans-serif; letter-spacing: 3px;
    color: var(--white);
  }
  .headliner {
    position: absolute; left: 0; right: 0; top: 486px; text-align: center;
    font: 400 50px/1 "Black Ops One", sans-serif; letter-spacing: 3px;
    color: var(--white);
  }
  .b2b {
    position: absolute; left: 0; right: 0; top: 540px; text-align: center;
    font: 400 16px/1 "Audiowide", sans-serif; letter-spacing: 3px;
    color: var(--cyan);
  }
  .co-headliner {
    position: absolute; left: 0; right: 0; top: 562px; text-align: center;
    font: 400 44px/1 "Audiowide", sans-serif; letter-spacing: 2px;
    color: var(--white); text-shadow: 0 0 12px rgba(95,214,236,.5);
  }
  .support {
    position: absolute; left: 0; right: 0; top: 616px; text-align: center;
    font: 400 30px/1 "Audiowide", sans-serif; letter-spacing: 2px;
    color: #d9eef0;
  }
  .details {
    position: absolute; left: 0; right: 0;
    font: 700 20px/1 "Saira Semi Condensed", sans-serif; letter-spacing: 1.5px;
    color: var(--white); text-align: center;
  }
  .details--row1 { top: 696px; }
  .details--row2 { top: 744px; }
  .details__accent { color: var(--sky); }
  .details__gap { display: inline-block; width: 70px; }
  .credit {
    position: absolute; left: 0; right: 0; top: 796px; text-align: center;
    font: 600 13px/1 "Saira Semi Condensed", sans-serif; letter-spacing: 2.5px;
    color: var(--muted);
  }
</style>
</head>
<body>
  <main class="flyer">
    <svg class="flyer__shapes" viewBox="0 0 594 840" aria-hidden="true">
      <polygon points="0,20 594,20 297,760" fill="none" stroke="#020607" stroke-width="34" opacity=".85"/>
      <polygon points="60,30 534,30 297,600" fill="none" stroke="#0f5a5d" stroke-width="6" opacity=".7"/>
      <polygon points="150,40 444,40 297,390" fill="#0a2f32" opacity=".6"/>
      <rect x="130" y="40" width="334" height="44" fill="#020607" opacity=".75"/>
      <rect x="0" y="672" width="594" height="168" fill="#020607"/>
      <polygon points="250,672 344,672 297,780" fill="#0d3d3f" opacity=".8"/>
    </svg>
    <div class="flyer__photo" role="img" aria-label="Photo of a DJ model in a cap with arms crossed, flanked by glowing speakers"></div>
    <p class="genre">HOUSE/TECHNO</p>
    <h1 class="host">Ripple</h1>
    <p class="presents">PRESENTS:</p>
    <h2 class="headliner">KORVEN</h2>
    <p class="b2b">B2B</p>
    <h2 class="co-headliner">MARTIN VOLKE</h2>
    <h3 class="support">+ TREVV LANE</h3>
    <p class="details details--row1">10/26/17<span class="details__gap"></span>21+<span class="details__gap"></span><span class="details__accent">10PM-2AM</span></p>
    <p class="details details--row2">2284 / HARLOW AVENUE / <span class="details__accent">SACRAMENTO / CA</span></p>
    <p class="credit">A BLUE CASCADE ENTERTAINMENT PRODUCTION</p>
  </main>
</body>
</html>
```